【概要】 住宅会社様の完成見学会のバナー制作です。 Web広告で使用するためのバナーデザインを募集します。 【依頼内容】 ・サイズ: 横1200× 縦628px、横1080× 縦1080px ・作成数: 1種類 ・利用用途:SNS広告(facebook/Instagram) 【目的】 完成見学会の来場促進(ぺージは下記) https://kanerudo.co.jp/ie/news/ie-news-8412-2-2-2-2-3-2-2-2-2-2-2-2/ 【デザインイメージ】 ・ターゲット層:30代~40代前半の主婦(若め)子供ができたばかり。旦那は普通の会社員。 ・雰囲気:お任せします 【使用素材】 添付のものをお使い下さい(全て使用しなくて結構です) ※開催日ですが、11/20.21は終了しているので削除し、残りの日程をバナーに表記してください。 【参考(クライアント)サイト】 https://kanerudo.co.jp https://hanamiho.com 【契約金額(税抜)】 3,000円/デザイン 最終納品のファイル形式は、AIもしくはPSDデータとしますが、デザイン提出段階では、PDFもしくはJPEGで問題ありません。 その他ご質問等ありましたら、気軽にお問い合わせください。 ご応募をお待ちしております! |
| https://kanerudo.co.jp/ie/news/ie-news-8412-2-2-2-2-3-2-2-2-2-2-2-2/ | ||

```html
<!DOCTYPE html>
<html lang="ja">
<head>
<meta charset="UTF-8">
<title>完成見学会 開催</title>
<link href="https://fonts.googleapis.com/css2?family=Noto+Sans+JP:wght@500;700;900&family=Roboto:wght@400;500&display=swap" rel="stylesheet">
<style>
  :root {
    --brown: #7b3a1c;
    --red: #e9544f;
    --white: #ffffff;
    --panel: rgba(58, 50, 46, 0.78);
    --band: rgba(255, 255, 255, 0.84);
    --sat: #8e9dff;
    --sun: #ff9aa6;
    --ink: #2b2b2b;
  }
  html, body { margin: 0; padding: 0; overflow: hidden; }
  body { width: 1200px; height: 1200px; font-family: "Noto Sans JP", sans-serif; }
  .banner { position: relative; width: 1200px; height: 1200px; overflow: hidden; }
  .interior-photo {
    position: absolute; inset: 0;
    background:
      linear-gradient(90deg, rgba(245,243,240,0.95) 0%, rgba(235,232,228,0.75) 14%, rgba(0,0,0,0) 28%),
      linear-gradient(180deg, #6e625a 0%, #8a7b70 22%, #a08a78 45%, #7a5238 62%, #c49a70 78%, #e2c49c 100%);
  }
  .brand {
    position: absolute; left: 40px; top: 32px; width: 560px; height: 115px;
    background: var(--white); display: flex; align-items: center; justify-content: center;
  }
  .brand-name { font-family: "Roboto", sans-serif; font-weight: 500; font-size: 72px; color: var(--ink); letter-spacing: 2px; }
  .headline-band {
    position: absolute; left: 0; top: 267px; width: 1200px; height: 146px; background: var(--band);
    display: flex; align-items: center; justify-content: center;
  }
  .headline { margin: 0; font-weight: 900; font-size: 124px; line-height: 1; color: var(--brown); letter-spacing: 4px; white-space: nowrap; }
  .tag {
    position: absolute; left: 90px; height: 72px; padding: 0 22px; background: var(--red); color: var(--white);
    border-radius: 12px; font-weight: 700; font-size: 44px; display: flex; align-items: center;
  }
  .tag-reservation { top: 482px; }
  .tag-limit { top: 590px; }
  .location { position: absolute; left: 452px; top: 470px; margin: 0; color: var(--white); font-weight: 700; font-size: 68px; letter-spacing: 3px; }
  .schedule {
    position: absolute; left: 326px; top: 700px; width: 660px; height: 395px; background: var(--panel);
    color: var(--white); font-family: "Roboto", "Noto Sans JP", sans-serif;
  }
  .date-line { position: absolute; left: 62px; font-size: 60px; font-weight: 400; white-space: nowrap; }
  .date-line .month { font-size: 44px; vertical-align: 14px; }
  .date-line .sat { color: var(--sat); font-weight: 500; }
  .date-line .sun { color: var(--sun); font-weight: 500; }
  .date-nov { top: 56px; }
  .date-dec { top: 142px; }
  .time { position: absolute; left: 0; width: 100%; top: 265px; text-align: center; font-size: 66px; }
</style>
</head>
<body>
<div class="banner">
  <div class="interior-photo" role="img" aria-label="木の床と革のソファ、ペンダント照明のある明るいリビングの写真"></div>

  <div class="brand">
    <span class="brand-name">kanerudo</span>
  </div>

  <div class="headline-band">
    <h1 class="headline">完成見学会 開催!</h1>
  </div>

  <div class="tag tag-reservation">完全予約制</div>
  <div class="tag tag-limit">1日4組様限定</div>
  <p class="location">富山市赤田</p>

  <div class="schedule">
    <div class="date-line date-nov"><span class="month">11</span>/27 <span class="sat">SAT</span> - 28 <span class="sun">SUN</span></div>
    <div class="date-line date-dec">12/04 <span class="sat">SAT</span> - 05 <span class="sun">SUN</span></div>
    <div class="time">10:00〜17:30</div>
  </div>
</div>
</body>
</html>
```